Bref créative
Ostravelde German Shepherds
West Bloodline German Shepherds
Bright & Fun-filled
Torsten Ebbelmann
287 Murow Rd
Suite F.
Portland, Tx 79152
torsten@ostravelde-kennel.example
www.ostravelde-kennel.example
Logo blown up, and some creativity.
Heres the logo. If you could make the German Shepherd text black that would be awesome. Currently with it being yellow it doesnt stick out enough. See what you can do. Thanks!
Not sure if zip file works? So just going to do this....

```html
<!DOCTYPE html>
<html lang="en">
<head>
<meta charset="utf-8">
<title>Ostravelde German Shepherds – Business Cards</title>
<link href="https://fonts.googleapis.com/css2?family=Montserrat:wght@500;700;800&display=swap" rel="stylesheet">
<style>
  :root {
    --bg: #e9e7e3;
    --yellow: #f4b512;
    --yellow-light: #fcd34a;
    --black: #1c1a19;
    --white: #ffffff;
    --paper: #f2f2f2;
    --grey: #6d6d6d;
    --shadow: rgba(0,0,0,0.18);
  }
  * { box-sizing: border-box; margin: 0; padding: 0; }
  html, body { width: 1200px; height: 926px; overflow: hidden; }
  body {
    background: var(--bg);
    font-family: "Montserrat", Arial, sans-serif;
    position: relative;
  }
  .card {
    position: absolute;
    width: 500px;
    height: 286px;
    border-radius: 24px;
    overflow: hidden;
    box-shadow: 0 10px 24px var(--shadow);
  }
  .card--contact { left: 70px;  top: 120px; background: var(--white); }
  .card--yellow  { left: 630px; top: 120px; background: linear-gradient(160deg, var(--yellow-light), var(--yellow) 70%); }
  .card--white   { left: 70px;  top: 520px; background: linear-gradient(160deg, var(--white), var(--paper)); }
  .card--black   { left: 630px; top: 520px; background: var(--black); }

  .card__shapes { position: absolute; inset: 0; width: 100%; height: 100%; }

  .brand {
    position: absolute;
    display: flex;
    flex-direction: column;
    align-items: center;
    text-align: center;
  }
  .brand__square {
    width: 52px; height: 52px;
    border-radius: 8px;
    background: var(--black);
    border: 5px solid var(--yellow);
    margin-bottom: 10px;
  }
  .brand__name {
    font-weight: 800;
    font-size: 24px;
    letter-spacing: 1px;
    line-height: 1.15;
    text-transform: uppercase;
    color: var(--black);
  }
  .brand__name small { display: block; font-size: 9px; letter-spacing: 3px; font-weight: 800; }
  .card--black .brand__name { color: var(--white); }
  .card--black .brand__square { background: var(--yellow); border-color: var(--black); }

  .card--contact .brand { left: 280px; top: 50px; width: 200px; }
  .card--yellow .brand,
  .card--white .brand,
  .card--black .brand { left: 0; right: 0; top: 66px; }

  .site {
    position: absolute;
    left: 0; right: 0;
    bottom: 62px;
    text-align: center;
    font-size: 12px;
    font-weight: 500;
    color: var(--grey);
  }
  .site::before { content: ""; display: inline-block; width: 6px; height: 6px; background: var(--yellow); margin-right: 6px; vertical-align: middle; }
  .card--yellow .site { color: var(--black); }
  .card--yellow .site::before { background: var(--black); }
  .card--black .site { color: #bdbdbd; }

  .holder {
    position: absolute;
    left: 24px; top: 74px;
    font-size: 11px;
    font-weight: 700;
    letter-spacing: 0.5px;
    text-transform: uppercase;
    color: var(--white);
    white-space: nowrap;
  }
  .contact {
    position: absolute;
    left: 50px; top: 152px;
    list-style: none;
    font-size: 10.5px;
    font-weight: 500;
    line-height: 18px;
    color: var(--black);
  }
  .contact li { position: relative; padding-left: 16px; }
  .contact li.icon::before {
    content: ""; position: absolute; left: 0; top: 5px;
    width: 8px; height: 8px; border-radius: 2px; background: var(--yellow);
  }
</style>
</head>
<body>

  <section class="card card--contact">
    <svg class="card__shapes" viewBox="0 0 500 286" aria-hidden="true">
      <path d="M0 0 H298 C272 82 215 126 0 144 Z" fill="var(--yellow)"/>
      <path d="M0 0 H280 C255 70 200 112 0 132 Z" fill="var(--black)"/>
      <path d="M500 130 V286 H330 C420 260 470 210 500 130 Z" fill="var(--yellow)"/>
      <path d="M500 160 V286 H370 C440 262 480 225 500 160 Z" fill="var(--black)"/>
    </svg>
    <p class="holder">Torsten Ebbelmann</p>
    <ul class="contact">
      <li class="icon">287 Murow Rd, Suite F.</li>
      <li>Portland, Tx 79152</li>
      <li class="icon">(555) 014-2281</li>
      <li class="icon">(555) 014-7730</li>
      <li class="icon">torsten@ostravelde-kennel.example</li>
      <li class="icon">www.ostravelde-kennel.example</li>
    </ul>
    <div class="brand">
      <span class="brand__square"></span>
      <p class="brand__name">Ostravelde<small>German Shepherds</small></p>
    </div>
  </section>

  <section class="card card--yellow">
    <div class="brand">
      <span class="brand__square"></span>
      <p class="brand__name">Ostravelde<small>German Shepherds</small></p>
    </div>
    <p class="site">www.ostravelde-kennel.example</p>
  </section>

  <section class="card card--white">
    <div class="brand">
      <span class="brand__square"></span>
      <p class="brand__name">Ostravelde<small>German Shepherds</small></p>
    </div>
    <p class="site">www.ostravelde-kennel.example</p>
  </section>

  <section class="card card--black">
    <div class="brand">
      <span class="brand__square"></span>
      <p class="brand__name">Ostravelde<small>German Shepherds</small></p>
    </div>
    <p class="site">www.ostravelde-kennel.example</p>
  </section>

</body>
</html>
```